R. T. HOLLOWAY, INC. is a US based Investment firm looking for a five-page website design.

Currently, their temporary site is located at: rtholloway.com and they would like to maintain the site design as much as possible.

R. T. HOLLOWAY, INC. sister companies are: Crestvale Lodge Investments (c-lodge.com) Benwick Petroleum (benwick-petroleum.com) and RTHF (rth-foundation.org/en)

Attached is a .ZIP file with designs and assets we think will be useful for your proposal… Content for the site is attached on: rtholloway website content.docx Current temp website design is attached as: Coming Soon Website.zip .EPS Logo files attached as: rtholloway logos.zip Sample business card attached as: R T Holloway Business cards.eps Other assets, such as Fonts and background images attached as: Assets.zip

Target Market(s)

Investors

Industry/Entity Type

Investments

Number of Pages Required

5+ page

Requirements
Must have
• Contact Page with a form.

```html
<!DOCTYPE html>
<html lang="en">
<head>
<meta charset="utf-8">
<title>R. T. HOLLOWAY, INC.</title>
<link href="https://fonts.googleapis.com/css2?family=Cinzel:wght@400;500&family=Cormorant+Garamond:wght@500;600&family=Lato:wght@400;700&display=swap" rel="stylesheet">
<style>
:root{
  --gold:#b39b5a;
  --gold-light:#c9b47c;
  --navy:#1f2a3c;
  --navy-deep:#18212f;
  --cream:#fdfbf4;
  --ink:#3a3a3a;
  --muted:#6b6b6b;
  --white:#ffffff;
  --line:#d8d2c2;
}
*{box-sizing:border-box;margin:0;padding:0}
html,body{width:1200px;height:4800px;overflow:hidden}
body{background:var(--cream);font-family:"Lato",sans-serif;color:var(--ink);position:relative}
.abs{position:absolute}
.serif{font-family:"Cinzel",serif;font-weight:400}

/* header */
.brand{left:106px;top:18px;width:210px;text-align:center}
.brand-mark{width:52px;height:52px;border:2px solid var(--gold);border-radius:50%;margin:0 auto 6px}
.brand-name{font-family:"Cinzel",serif;font-size:25px;color:var(--navy);letter-spacing:1px;line-height:1.1}
.brand-name span{display:block;font-size:14px}
.contact-item{top:44px;display:flex;align-items:center;gap:12px}
.contact-icon{width:38px;height:38px;border-radius:50%;background:var(--navy);display:flex;align-items:center;justify-content:center}
.contact-label{font-size:13px;color:var(--gold);font-weight:700;letter-spacing:.5px}
.contact-value{font-size:14px;color:var(--navy)}

.nav{left:0;top:134px;width:1200px;height:60px;background:var(--gold)}
.nav a{position:absolute;top:0;height:60px;line-height:60px;color:var(--white);font-size:13px;letter-spacing:.5px;text-decoration:none;text-align:center;transform:translateX(-50%)}
.nav a.active{background:var(--navy);width:146px;transform:none;left:106px}
.nav .sep{position:absolute;top:20px;width:1px;height:20px;background:rgba(255,255,255,.35)}

/* hero */
.hero-text{left:106px;top:438px;color:var(--white)}
.hero-kicker{font-family:"Cinzel",serif;font-size:20px;letter-spacing:1px}
.hero-title{font-family:"Cinzel",serif;font-size:36px;letter-spacing:1px;margin-top:6px}
.hero-desc{font-size:14px;line-height:21px;margin-top:8px;width:400px}

.btn{position:absolute;height:44px;border-radius:22px;background:var(--gold);color:var(--white);font-size:14px;display:flex;align-items:center;padding-left:26px}
.btn i{position:absolute;right:8px;top:9px;width:26px;height:26px;border-radius:50%;background:var(--navy);display:flex;align-items:center;justify-content:center}

.hero-dots{left:1154px;top:474px}
.hero-dots b{display:block;width:11px;height:11px;border-radius:50%;background:var(--gold);margin-bottom:9px}
.hero-num{left:1118px;top:506px;font-size:11px;color:var(--white);transform:rotate(90deg)}
.scroll-cue{left:576px;top:914px;width:44px;height:56px;border-radius:22px;background:var(--white);border:1px solid var(--line);display:flex;align-items:center;justify-content:center}

/* feature tiles */
.tile{top:1058px;width:200px;height:185px;border-radius:22px;background:var(--gold);color:var(--white);text-align:center}
.tile.dark{background:var(--navy)}
.tile svg{margin-top:26px}
.tile-label{position:absolute;left:0;right:0;bottom:30px;font-family:"Cinzel",serif;font-size:17px;letter-spacing:.5px}

/* headings */
.section-title{font-family:"Cinzel",serif;font-size:35px;color:var(--navy);letter-spacing:1px;text-align:center;left:0;width:1200px}
.rule{height:2px;width:78px;background:var(--gold)}

/* about */
.about-ring{left:94px;top:1378px;width:486px;height:486px;border-radius:50%;border:1px solid #e6e0d0}
.about-photo{left:104px;top:1388px;width:466px;height:466px;border-radius:50%;background:radial-gradient(circle at 45% 40%,#c59a78 0%,#6a7a92 40%,#27344a 100%)}
.badge{left:444px;top:1407px;width:130px;height:130px;border-radius:50%;background:var(--gold);border:5px solid var(--cream);box-shadow:0 0 0 1px var(--line);color:var(--white);text-align:center;padding-top:26px}
.badge-num{font-family:"Cinzel",serif;font-size:40px;line-height:40px;display:inline-block;vertical-align:top}
.badge-text{font-family:"Cinzel",serif;font-size:15px;line-height:18px}
.about-copy{left:626px;top:1404px;width:470px}
.about-kicker{font-size:13px;color:var(--gold);font-weight:700}
.copy{font-size:13px;line-height:30px;color:var(--ink)}

/* investment areas */
.card{width:313px;height:433px;background:var(--white);border-radius:10px;overflow:hidden;box-shadow:0 2px 6px rgba(0,0,0,.08);text-align:center}
.card-photo{height:227px;width:100%}
.card-icon{position:absolute;left:131px;top:197px;width:52px;height:52px;border-radius:50%;background:var(--white);display:flex;align-items:center;justify-content:center}
.card-title{font-family:"Cinzel",serif;font-size:18px;color:var(--navy);margin-top:34px;letter-spacing:.5px}
.card-text{font-size:13px;line-height:18px;color:var(--muted);margin:16px auto 0;width:250px}
.card-arrow{margin-top:24px}

/* social */
.social-copy{left:106px;top:3172px;width:480px}
.social-title{font-family:"Cinzel",serif;font-size:35px;color:var(--navy);letter-spacing:1px}
.copy a{color:#4a72b8;text-decoration:none}
.dots{left:650px;top:3180px;width:440px;height:420px;background-image:radial-gradient(#d4cdb9 1.3px,transparent 1.4px);background-size:10px 10px}
.social-ring{left:612px;top:3146px;width:478px;height:478px;border-radius:50%;border:1px solid #e6e0d0;background:var(--cream)}
.social-photo{left:620px;top:3154px;width:462px;height:462px;border-radius:50%;background:linear-gradient(180deg,#7fa6c9 0%,#b8a6a6 38%,#8d6a4e 62%,#3f3326 100%)}

/* contact */
.subtitle{left:0;width:1200px;text-align:center;font-size:13px;color:var(--muted)}
.field{height:45px;border:1px solid #cfcabb;background:var(--cream);font-size:13px;color:var(--muted);padding:14px 12px}

/* footer */
.footer-col h4{font-family:"Cormorant Garamond",serif;font-weight:600;font-size:19px;color:var(--white);margin-bottom:14px}
.footer-col h4:after{content:"";display:block;width:40px;height:1px;background:var(--gold);margin-top:4px}
.footer-brand .brand-name{color:var(--white)}
.f-row{display:flex;gap:18px;color:var(--white);font-size:11px;line-height:17px;margin-bottom:12px}
.links li{list-style:none;color:var(--white);font-size:11px;line-height:30px}
.links li:before{content:"›";color:var(--gold);margin-right:14px}
.news-text{color:var(--white);font-size:11px;line-height:30px}
.news-input{width:201px;height:42px;border-radius:21px;background:var(--white);font-size:11px;color:var(--muted);padding:14px 22px;margin-top:4px}
.news-btn{width:201px;height:42px;border-radius:21px;background:var(--gold);color:var(--white);font-size:10px;text-align:center;line-height:42px;margin-top:16px}
.map{left:851px;top:4440px;width:239px;height:164px;background:linear-gradient(135deg,#e7ebe2,#cfd8d6);border:5px solid var(--white)}
.copyright{left:106px;top:4743px;font-size:13px;color:var(--muted)}
.copyright b{color:var(--gold);font-weight:400}
.social-dot{top:4734px;width:34px;height:34px;border-radius:50%;background:var(--gold)}
.social-dot.dark{background:var(--navy)}
</style>
</head>
<body>

<!-- header -->
<div class="abs brand">
  <div class="brand-mark"></div>
  <div class="brand-name">R. T. HOLLOWAY<span>INC.</span></div>
</div>
<div class="abs contact-item" style="left:730px">
  <div class="contact-icon"><svg width="16" height="16" viewBox="0 0 16 16"><path d="M3 1l3 3-2 2c1 2 3 4 5 5l2-2 3 3-2 3C7 15 1 9 0 3z" fill="#fff"/></svg></div>
  <div><div class="contact-label">CALL US</div><div class="contact-value">123 456 7890</div></div>
</div>
<div class="abs contact-item" style="left:894px">
  <div class="contact-icon"><svg width="16" height="12" viewBox="0 0 16 12"><rect width="16" height="12" rx="1" fill="#fff"/><path d="M0 1l8 6 8-6" stroke="#1f2a3c" fill="none" stroke-width="1.4"/></svg></div>
  <div><div class="contact-label">EMAIL US</div><div class="contact-value">name@rtholloway.com</div></div>
</div>

<nav class="abs nav">
  <a class="active">HOME</a>
  <a style="left:341px">ABOUT US</a><span class="sep" style="left:426px"></span>
  <a style="left:553px">INVESTMENT AREAS</a><span class="sep" style="left:684px"></span>
  <a style="left:812px">SOCIAL RESPONSIBILITY</a><span class="sep" style="left:946px"></span>
  <a style="left:1045px">CONTACT US</a>
</nav>

<!-- hero -->
<svg class="abs" style="left:0;top:194px" width="1200" height="780" viewBox="0 0 1200 780">
  <defs>
    <linearGradient id="heroFill" x1="0" y1="0" x2="1" y2="1">
      <stop offset="0" stop-color="#4d5b70"/>
      <stop offset=".45" stop-color="#2a3547"/>
      <stop offset=".75" stop-color="#5c4a32"/>
      <stop offset="1" stop-color="#1b2433"/>
    </linearGradient>
  </defs>
  <polygon role="img" aria-label="Businessman with clasped hands behind stacks of coins and a jar with a sprouting plant" points="0,0 1200,0 1200,732 615,756 0,778" fill="url(#heroFill)"/>
  <polygon points="615,756 1200,732 1200,778" fill="#b39b5a"/>
</svg>
<div class="abs hero-text">
  <div class="hero-kicker">WELCOME TO</div>
  <div class="hero-title">R. T. HOLLOWAY, INC.</div>
  <p class="hero-desc">R. T. Holloway, Inc. helps develop into a great nation and, with assertiveness, stamp its footprint worldwide.</p>
</div>
<div class="btn" style="left:106px;top:590px;width:149px">Read More<i><svg width="10" height="10" viewBox="0 0 10 10"><path d="M1 5h8M5 1l4 4-4 4" stroke="#fff" fill="none" stroke-width="1.4"/></svg></i></div>
<div class="abs hero-dots"><b></b><b></b><b></b></div>
<div class="abs hero-num">02</div>
<div class="abs scroll-cue"><svg width="14" height="30" viewBox="0 0 14 30"><path d="M7 2v26M2 23l5 5 5-5" stroke="#1f2a3c" fill="none" stroke-width="1.5"/></svg></div>

<!-- tiles -->
<div class="abs tile" style="left:142px">
  <svg width="96" height="70" viewBox="0 0 96 70" fill="none" stroke="#fff" stroke-width="2.2"><path d="M2 66l28-30 12 12 16-26 36 44"/><path d="M58 22V2l14 5-14 5"/><path d="M30 36l6 10 6-4"/></svg>
  <div class="tile-label">MISSION</div>
</div>
<div class="abs tile dark" style="left:380px">
  <svg width="70" height="76" viewBox="0 0 70 76" fill="none" stroke="#b39b5a" stroke-width="2.2"><path d="M35 18a17 17 0 0 0-10 31v9h20v-9a17 17 0 0 0-10-31z"/><path d="M27 64h16M29 70h12M35 38v20M29 44l6-6 6 6"/><path d="M35 2v8M8 12l6 6M62 12l-6 6"/></svg>
  <div class="tile-label">VISION</div>
</div>
<div class="abs tile" style="left:618px">
  <svg width="92" height="76" viewBox="0 0 92 76" fill="none" stroke="#fff" stroke-width="2.2"><path d="M18 18h56l14 16-42 40L4 34z"/><path d="M4 34h84M30 18l-8 16 24 40 24-40-8-16M46 18l-16 16M46 18l16 16"/><path d="M46 2v8M22 6l4 7M70 6l-4 7"/></svg>
  <div class="tile-label">VALUES</div>
</div>
<div class="abs tile" style="left:857px">
  <svg width="92" height="76" viewBox="0 0 92 76" fill="none" stroke="#fff" stroke-width="2.2"><circle cx="46" cy="10" r="6"/><circle cx="22" cy="26" r="6"/><circle cx="70" cy="26" r="6"/><path d="M38 40V22h16v18M14 56V38h16v18M62 56V38h16v18M4 74V58h84v16"/><path d="M40 40v16M52 40v16"/></svg>
  <div class="tile-label">LEADERSHIP</div>
</div>

<!-- about -->
<h2 class="abs section-title" style="top:1322px">ABOUT US</h2>
<div class="abs about-ring"></div>
<div class="abs about-photo" role="img" aria-label="Two business people shaking hands"></div>
<div class="abs badge"><span class="badge-num">11</span><span class="badge-text" style="vertical-align:top;display:inline-block;margin-top:16px"> YEAR</span><div class="badge-text">EXPERIENCE</div></div>
<div class="abs about-copy">
  <div class="about-kicker">BASED IN HOUSTON, TEXAS, R. T. HOLLOWAY, INC.</div>
  <div class="rule" style="margin:12px 0 14px"></div>
  <p class="copy">Based in Houston, Texas, R. T. Holloway, Inc. is an investment company, founded in 2010, with the purpose to foster endeavors for socioeconomic development, and create platforms for harnessing the potential of world resources, designed to meet the demands of the emerging markets. R. T. Holloway, Inc. functions as a vehicle that enables investments, with the goal of developing the multiple opportunities available.</p>
  <p class="copy" style="margin-top:30px">R. T. Holloway, Inc. holds interests in areas of investment that are vital to the international economy: Sectors of Energy, Mining, Industry, Finance and Real Estate.</p>
</div>
<div class="btn" style="left:622px;top:1779px;width:172px;padding-left:44px">Read More<i><svg width="10" height="10" viewBox="0 0 10 10"><path d="M1 5h8M5 1l4 4-4 4" stroke="#fff" fill="none" stroke-width="1.4"/></svg></i></div>

<!-- investment areas -->
<svg class="abs" style="left:0;top:1900px" width="1200" height="990" viewBox="0 0 1200 990">
  <polygon points="0,62 1200,4 1200,890 0,980" fill="#b39b5a"/>
</svg>
<h2 class="abs section-title" style="top:2000px;color:var(--white)">INVESTMENT AREAS</h2>

<div class="abs card" style="left:106px;top:2075px">
  <div class="card-photo" role="img" aria-label="Wind turbines and solar panels in a valley" style="background:linear-gradient(160deg,#cfe0ef,#6f93b8 55%,#3f6a4a)"></div>
  <div class="card-icon"><svg width="28" height="28" viewBox="0 0 28 28" fill="none" stroke="#b39b5a" stroke-width="1.5"><rect x="5" y="6" width="12" height="20"/><rect x="17" y="12" width="7" height="14"/><path d="M8 10h6M8 14h6M8 18h6M2 26h24"/></svg></div>
  <div class="card-title">ENERGY</div>
  <p class="card-text">R. T. Holloway, Inc. holds investments both in Exploration &amp; Production, and support field services...</p>
  <div class="card-arrow"><svg width="34" height="12" viewBox="0 0 34 12"><path d="M1 6h31M27 1l5 5-5 5" stroke="#1f2a3c" fill="none" stroke-width="1.5"/></svg></div>
</div>
<div class="abs card" style="left:443px;top:2075px">
  <div class="card-photo" role="img" aria-label="Excavator loading a mining truck in a quarry" style="background:linear-gradient(170deg,#9c9486,#6e6253 55%,#c2952e)"></div>
  <div class="card-icon"><svg width="28" height="28" viewBox="0 0 28 28" fill="none" stroke="#b39b5a" stroke-width="1.5"><path d="M4 24L20 8M14 4c6 0 10 4 10 10M10 6l12 12M3 26h22"/></svg></div>
  <div class="card-title">MINING</div>
  <p class="card-text">R. T. Holloway, Inc. holds investments both in Exploration &amp; Production, and support field services...</p>
  <div class="card-arrow"><svg width="34" height="12" viewBox="0 0 34 12"><path d="M1 6h31M27 1l5 5-5 5" stroke="#1f2a3c" fill="none" stroke-width="1.5"/></svg></div>
</div>
<div class="abs card" style="left:779px;top:2075px">
  <div class="card-photo" role="img" aria-label="Industrial plant with chimneys at dusk" style="background:linear-gradient(175deg,#7f9fc4,#46607e 55%,#263349)"></div>
  <div class="card-icon"><svg width="28" height="28" viewBox="0 0 28 28" fill="none" stroke="#b39b5a" stroke-width="1.5"><path d="M3 26V14l7 4v-4l7 4v-4l7 4v8zM20 14V4h4v12"/><path d="M7 22h3M13 22h3M19 22h3"/></svg></div>
  <div class="card-title">INDUSTRY</div>
  <p class="card-text">R. T. Holloway, Inc. holds investments both in Exploration &amp; Production, and support field services...</p>
  <div class="card-arrow"><svg width="34" height="12" viewBox="0 0 34 12"><path d="M1 6h31M27 1l5 5-5 5" stroke="#1f2a3c" fill="none" stroke-width="1.5"/></svg></div>
</div>

<div class="abs card" style="left:106px;top:2549px">
  <div class="card-photo" role="img" aria-label="Hands using a calculator on a desk" style="background:linear-gradient(160deg,#dedbd6,#9e9a95 55%,#4e4a47)"></div>
  <div class="card-icon"><svg width="28" height="28" viewBox="0 0 28 28" fill="none" stroke="#b39b5a" stroke-width="1.5"><circle cx="11" cy="17" r="8"/><circle cx="20" cy="20" r="5"/><path d="M8 5h6l-2 4h-2z"/></svg></div>
  <div class="card-title">FINANCE</div>
  <p class="card-text">R. T. Holloway, Inc. holds investments both in Exploration &amp; Production, and support field services...</p>
  <div class="card-arrow"><svg width="34" height="12" viewBox="0 0 34 12"><path d="M1 6h31M27 1l5 5-5 5" stroke="#1f2a3c" fill="none" stroke-width="1.5"/></svg></div>
</div>
<div class="abs card" style="left:443px;top:2549px">
  <div class="card-photo" role="img" aria-label="Empty hospital operating room" style="background:linear-gradient(170deg,#cfe1e6,#7fa4ae 55%,#4a6570)"></div>
  <div class="card-icon"><svg width="28" height="28" viewBox="0 0 28 28" fill="none" stroke="#b39b5a" stroke-width="1.5"><path d="M14 24S3 17 3 10a5.5 5.5 0 0 1 11-1 5.5 5.5 0 0 1 11 1c0 7-11 14-11 14z"/><path d="M6 14h5l2-3 3 6 2-3h4"/></svg></div>
  <div class="card-title">HEALTHCARE</div>
  <p class="card-text">R. T. Holloway, Inc. holds investments both in Exploration &amp; Production, and support field services...</p>
  <div class="card-arrow"><svg width="34" height="12" viewBox="0 0 34 12"><path d="M1 6h31M27 1l5 5-5 5" stroke="#1f2a3c" fill="none" stroke-width="1.5"/></svg></div>
</div>
<div class="abs card" style="left:779px;top:2549px">
  <div class="card-photo" role="img" aria-label="Modern glass office building against blue sky" style="background:linear-gradient(160deg,#9cc0e4,#5f86b2 55%,#2c3e58)"></div>
  <div class="card-icon"><svg width="28" height="28" viewBox="0 0 28 28" fill="none" stroke="#b39b5a" stroke-width="1.5"><path d="M3 13L14 4l11 9M6 11v14h16V11"/><rect x="11" y="17" width="6" height="8"/></svg></div>
  <div class="card-title">REAL ESTATE</div>
  <p class="card-text">R. T. Holloway, Inc. holds investments both in Exploration &amp; Production, and support field services...</p>
  <div class="card-arrow"><svg width="34" height="12" viewBox="0 0 34 12"><path d="M1 6h31M27 1l5 5-5 5" stroke="#1f2a3c" fill="none" stroke-width="1.5"/></svg></div>
</div>
<div class="btn" style="left:514px;top:3020px;width:172px;padding-left:44px">View More<i><svg width="10" height="10" viewBox="0 0 10 10"><path d="M1 5h8M5 1l4 4-4 4" stroke="#fff" fill="none" stroke-width="1.4"/></svg></i></div>

<!-- social responsibility -->
<div class="abs social-copy">
  <h2 class="social-title">SOCIAL RESPONSIBILITY</h2>
  <div class="rule" style="margin:10px 0 16px"></div>
  <p class="copy">Since the commencement of our activity, R. T. Holloway, Inc. contributes to change the quality of life of children and seniors across the world, providing them with support for primary education and basic medical aid, which we believe to be the right of every human being.</p>
  <p class="copy" style="margin-top:30px">Proportionally to our growth, R. T. Holloway, Inc. aims to extend our contributions to other communities in Africa and the rest of the World, with more donations to charities and other non-profit organizations via the Rowan T. Holloway Foundation <a>(https://rth-foundation.org/en/)</a></p>
</div>
<div class="btn" style="left:106px;top:3525px;width:149px">Read More<i><svg width="10" height="10" viewBox="0 0 10 10"><path d="M1 5h8M5 1l4 4-4 4" stroke="#fff" fill="none" stroke-width="1.4"/></svg></i></div>
<div class="abs dots"></div>
<div class="abs social-ring"></div>
<div class="abs social-photo" role="img" aria-label="Rocky mountain cliffs above a misty valley at sunset"></div>

<!-- contact -->
<h2 class="abs section-title" style="top:3718px">GET IN TOUCH</h2>
<div class="abs subtitle" style="top:3768px">Quick Contact</div>
<div class="abs field" style="left:292px;top:3810px;width:297px">First Name</div>
<div class="abs field" style="left:609px;top:3810px;width:298px">Last Name</div>
<div class="abs field" style="left:292px;top:3871px;width:297px">Email</div>
<div class="abs field" style="left:609px;top:3871px;width:298px">Phone</div>
<div class="abs field" style="left:292px;top:3933px;width:615px;height:158px">Message</div>
<div class="btn" style="left:525px;top:4125px;width:149px;padding-left:55px">Send<i><svg width="10" height="10" viewBox="0 0 10 10"><path d="M1 5h8M5 1l4 4-4 4" stroke="#fff" fill="none" stroke-width="1.4"/></svg></i></div>

<!-- footer -->
<svg class="abs" style="left:0;top:4200px" width="1200" height="520" viewBox="0 0 1200 520">
  <polygon points="0,22 1200,62 1200,72 0,92" fill="#b39b5a"/>
  <polygon points="0,90 1200,70 1200,513 0,513" fill="#1f2a3c"/>
</svg>
<div class="abs brand footer-brand" style="top:4376px">
  <div class="brand-mark"></div>
  <div class="brand-name">R. T. HOLLOWAY<span>INC.</span></div>
</div>
<div class="abs" style="left:120px;top:4492px;width:220px">
  <div class="f-row"><svg width="12" height="16" viewBox="0 0 12 16"><path d="M6 0a6 6 0 0 0-6 6c0 4 6 10 6 10s6-6 6-10a6 6 0 0 0-6-6z" fill="#b39b5a"/><circle cx="6" cy="6" r="2" fill="#1f2a3c"/></svg><span>2210 Larkmoor Ave, 9th Floor<br><br>Houston, Tx 77057</span></div>
  <div class="f-row" style="margin-top:4px"><svg width="12" height="12" viewBox="0 0 16 16"><path d="M3 1l3 3-2 2c1 2 3 4 5 5l2-2 3 3-2 3C7 15 1 9 0 3z" fill="#b39b5a"/></svg><span>+1 (123) 456 7890</span></div>
  <div class="f-row"><svg width="14" height="11" viewBox="0 0 16 12"><rect width="16" height="12" fill="#b39b5a"/><path d="M0 1l8 6 8-6" stroke="#1f2a3c" fill="none"/></svg><span>name@rtholloway.com</span></div>
</div>
<div class="abs footer-col" style="left:382px;top:4386px">
  <h4>Quick Link</h4>
  <ul class="links" style="margin-top:-4px">
    <li>HOME</li><li>ABOUT US</li><li>INVESTMENT AREAS</li><li>SOCIAL RESPONSIBILITY</li><li>CONTACT US</li>
  </ul>
</div>
<div class="abs footer-col" style="left:600px;top:4386px;width:210px">
  <h4>Newsletter</h4>
  <p class="news-text" style="margin-top:-4px">Join Our Newsletter to receive the latest update and promotion.</p>
  <div class="news-input">Your Email</div>
  <div class="news-btn">SUBSCRIBE</div>
</div>
<div class="abs footer-col" style="left:851px;top:4386px"><h4>Map</h4></div>
<div class="abs map" role="img" aria-label="Map of the United States marking the Houston office"></div>

<div class="abs copyright">Copyright © 2021 <b>R T HOLLOWAY INC</b>, All Rights Reserved.</div>
<div class="abs social-dot" style="left:920px" role="img" aria-label="Social profile link"></div>
<div class="abs social-dot dark" style="left:965px" role="img" aria-label="Social profile link"></div>
<div class="abs social-dot dark" style="left:1010px" role="img" aria-label="Social profile link"></div>
<div class="abs social-dot dark" style="left:1056px" role="img" aria-label="Social profile link"></div>

</body>
</html>
```